Business Card Designs

Looking to design a 3.5" x 2" standard business card for our employees.
The design needs to be sleek, simple, and modern. We would like our logo (attached) to be incorporated, but not in that colour, rather an outline of the logo in either gold or silver (whichever looks better).

Modern and Simple is what we are looking for, but be creative in incorporating the logo.

```html
<!DOCTYPE html>
<html lang="en">
<head>
<meta charset="utf-8">
<title>Harbourline Residences – Business Card</title>
<link href="https://fonts.googleapis.com/css2?family=Arimo:wght@400;700&display=swap" rel="stylesheet">
<style>
  :root{
    --backdrop:#e9e6e1;
    --card:#1e1d1f;
    --teal:#5a9a9a;
    --teal-light:#7fbcbc;
    --ink:#1b1b1b;
    --text:#e7e7e7;
    --silver-1:#f4f4f4;
    --silver-2:#b9b9b9;
    --silver-3:#8c8c8c;
  }
  *{margin:0;padding:0;box-sizing:border-box}
  html,body{width:1200px;height:900px;overflow:hidden}
  body{background:var(--backdrop);font-family:"Arimo",Arial,sans-serif;position:relative}
  .card{
    position:absolute;width:540px;height:309px;background:var(--card);
    overflow:hidden;box-shadow:0 10px 30px rgba(0,0,0,.25);
  }
  .card--front{left:40px;top:296px}
  .card--back{left:620px;top:296px}
  .card__trim{position:absolute;inset:0;width:100%;height:100%}
  .brand{
    position:absolute;color:var(--teal-light);font-weight:700;
    text-transform:uppercase;letter-spacing:2px;line-height:1.15;text-align:right;
    display:flex;align-items:center;gap:10px;
  }
  .brand__mark{width:14px;height:14px;background:var(--teal-light);flex:none}
  .card--front .brand{right:44px;top:92px;font-size:22px}
  .card--back .brand{right:40px;top:40px;font-size:17px}
  .url{
    position:absolute;color:var(--ink);font-weight:700;font-size:13px;letter-spacing:2px;
    white-space:nowrap;
  }
  .card--front .url{left:24px;bottom:22px}
  .card--back .url{left:366px;top:222px}
  .person{position:absolute;left:34px;top:150px}
  .person__name{color:var(--teal-light);font-size:20px;letter-spacing:1px;text-transform:uppercase}
  .person__role{color:var(--text);font-size:14px;margin-top:4px}
  .contact{position:absolute;color:var(--text);font-size:13px;line-height:1.5;white-space:nowrap}
  .contact--direct{left:34px;top:228px}
  .contact--address{left:200px;top:204px}
  .contact__row{display:flex;align-items:flex-start;gap:8px}
  .contact__icon{width:13px;height:13px;margin-top:3px;flex:none}
</style>
</head>
<body>

<section class="card card--front" aria-label="Card front">
  <svg class="card__trim" viewBox="0 0 540 309" aria-hidden="true">
    <defs>
      <linearGradient id="silverFront" x1="0" y1="0" x2="1" y2="0">
        <stop offset="0" stop-color="var(--silver-2)"/>
        <stop offset=".35" stop-color="var(--silver-1)"/>
        <stop offset=".7" stop-color="var(--silver-3)"/>
        <stop offset="1" stop-color="var(--silver-1)"/>
      </linearGradient>
    </defs>
    <path d="M0 256 H214 L240 284 H540 V309 H0 Z" fill="url(#silverFront)"/>
    <path d="M0 253 H215 L241 281 H540" fill="none" stroke="var(--teal)" stroke-width="2"/>
  </svg>
  <div class="brand"><span class="brand__mark"></span><span>Harbourline<br>Residences</span></div>
  <div class="url">www.harbourline.co</div>
</section>

<section class="card card--back" aria-label="Card back">
  <svg class="card__trim" viewBox="0 0 540 309" aria-hidden="true">
    <defs>
      <linearGradient id="silverBack" x1="0" y1="0" x2="1" y2="0">
        <stop offset="0" stop-color="var(--silver-3)"/>
        <stop offset=".4" stop-color="var(--silver-1)"/>
        <stop offset=".75" stop-color="var(--silver-2)"/>
        <stop offset="1" stop-color="var(--silver-1)"/>
      </linearGradient>
    </defs>
    <path d="M0 292 H328 L352 192 H540 V309 H0 Z" fill="url(#silverBack)"/>
    <path d="M0 289 H326 L350 189 H540" fill="none" stroke="var(--teal)" stroke-width="2"/>
  </svg>
  <div class="brand"><span class="brand__mark"></span><span>Harbourline<br>Residences</span></div>
  <div class="url">www.harbourline.co</div>

  <div class="person">
    <div class="person__name">Elena Marsh</div>
    <div class="person__role">Director</div>
  </div>

  <div class="contact contact--direct">
    <div class="contact__row">
      <svg class="contact__icon" viewBox="0 0 16 16" aria-hidden="true"><path fill="var(--teal)" d="M3 1h3l1.5 4-2 1.3a9 9 0 0 0 4.2 4.2L11 8.5l4 1.5v3a2 2 0 0 1-2 2A12 12 0 0 1 1 3a2 2 0 0 1 2-2z"/></svg>
      <span>555-014-2286</span>
    </div>
    <div class="contact__row">
      <svg class="contact__icon" viewBox="0 0 16 16" aria-hidden="true"><rect x="1" y="3" width="14" height="10" rx="1" fill="var(--teal)"/><path d="M1.5 4 8 9l6.5-5" fill="none" stroke="var(--card)" stroke-width="1.4"/></svg>
      <span>hello@harbourline.co</span>
    </div>
  </div>

  <div class="contact contact--address">
    <div class="contact__row">
      <svg class="contact__icon" viewBox="0 0 16 16" aria-hidden="true"><path fill="var(--teal)" d="M8 0a5.5 5.5 0 0 0-5.5 5.5C2.5 10 8 16 8 16s5.5-6 5.5-10.5A5.5 5.5 0 0 0 8 0zm0 8a2.5 2.5 0 1 1 0-5 2.5 2.5 0 0 1 0 5z"/></svg>
      <span>42 Orchard Lane<br>Westbrook 0000</span>
    </div>
  </div>
</section>

</body>
</html>
```